Australian Based Booking Platform Needs Playful Home Page & Profile Page To Showcase Our Acti...

COMPANY OVERVIEW:
WAVELOOP TRIPS is an Australian based activity booking platform. Our point of difference is our Kiosk machines that are located in hotels around Australia and allow customers instant access to book activities from the hotel reception.

HOME PAGE:
This page needs to clearly show that we are Australia’s leading booking platform.
Our Competition: https://www.roamquill.com.au/en
IMPORTANT SECTIONS ON THE HOME PAGE:
- Key Bullet Points (Best Price Guaranteed, Trusted By Thousands, Australian Owned, Unbeatable Support)
- Top Experiences – (Images of selected experiences in a slider format)
- Take Me There – Gold Coast, Carins, Port Duglas, Sunshine Coast, Whitsundays, Brisbane, Sydney, Adelaide, Hobart, Perth
- Top Deals For You – (Images of selected experiences in a slider format)
- Experiences You’ll Love – (Categories of Adventure Tours, Outdoor Activities, Hot Deals, Fun & Games, Zoos & Aquariums, Reef & Island Cruises)
- Testimonials – (some sort of slider format)
- Top New Experience – (Images of selected experiences in a slider format)
- Footer Menu
NOTE: Including some sort of mascot on the page to introduce a personality would be amazing. A Kangaroo or Koala could be a good choice.

REGION PAGE:
This page needs to clearly show what is on offer in the region. The layout of this page will be used for all regions in Australia (eg Gold Coast, Carins, Port Duglas, Sunshine Coast, Whitsundays, Brisbane, Sydney, Adelaide, Hobart, Perth)
IMPORTANT SECTIONS ON THE REGION PAGE:
- Categories: Adventure Tours, Outdoor Activities, Hot Deals, Fun & Games, Zoos & Aquariums, Reef & Island Cruises
o This Categories menu allows you to flick between sliders with activities from the different categories
- Footer Menu

PROFILE PAGE:
The layout of this page is going to be used to clearly show off every activity people can book.
Competitors Example:
https://www.trekvanta.com/tours/Sydney/Sydney-Harbour-Northern-beaches-and-National-Park/d357-137441P2
https://www.roamquill.com.au/en/gold-coast/pelwin-isle-dolphin-and-marrabin-reef-snorkelling-cruise
IMPORTANT SECTIONS ON THE PROFILE PAGE:
- Tour Title
- Photos / Video
- Booking Calanda (As displayed on the above link)
- Highlights & Inclusions
- Overview
- Location (Map)
- What To Bring
- Additional Information
- Booking Information
- Reviews:
- Terms & Conditions
NOTE: This page is to be displayed on a kiosk with the following dimensions;
- 1209.8mm x 680.4mm
- Aspect Ratio 16:9

I have uploaded some images of Australia, as well as our logo. Please feel free to use or not use these images as you decide.

Keep up the good work on the designs :)

Target Market(s)

Australian Holiday Makers

Industry/Entity Type

Tourism Booking Platform

Number of Pages Required

3 page

Font styles to use
Sans Serif

Requirements
Must have
• - This booking calendar https://app.clipvessel.com/fFoAUeq8Hhpn4
Nice to have
• A mascot or something to add character to the page.

```html
<!DOCTYPE html>
<html lang="en">
<head>
<meta charset="utf-8">
<title>WAVELOOP TRIPS – Experience It All</title>
<link href="https://fonts.googleapis.com/css2?family=Poppins:wght@400;500;600;700&display=swap" rel="stylesheet">
<style>
:root{
  --yellow:#f9b91a;
  --orange:#f7a21b;
  --accent:#f15a24;
  --ink:#111111;
  --text:#2b2b2b;
  --muted:#777777;
  --grey-bg:#f3f3f3;
  --beige:#fbeed5;
  --white:#ffffff;
}
*{box-sizing:border-box;margin:0;padding:0}
html,body{width:1200px;height:5352px;overflow:hidden}
body{font-family:'Poppins',sans-serif;color:var(--text);background:var(--white);position:relative}
.section{position:absolute;left:0;width:1200px}
.abs{position:absolute}

/* header */
.site-header{top:0;height:80px;background:var(--white);box-shadow:0 1px 4px rgba(0,0,0,.06);z-index:5}
.menu-toggle{left:112px;top:25px;width:30px;height:30px;border:2px solid var(--ink);border-radius:4px;display:flex;flex-direction:column;justify-content:center;align-items:center;gap:4px}
.menu-toggle span{width:14px;height:2px;background:var(--ink)}
.brand{left:176px;top:22px;font-size:24px;font-weight:700;color:var(--ink);letter-spacing:1px}
.main-nav{left:462px;top:28px;display:flex;gap:20px;font-size:14px;color:var(--ink)}
.main-nav .hot{color:var(--accent)}
.login{left:930px;top:24px;width:82px;height:32px;border-radius:16px;background:var(--yellow);font-size:11px;display:flex;align-items:center;padding-left:14px;gap:8px}
.login i{width:22px;height:22px;border-radius:50%;background:var(--ink);display:block}
.head-icon{top:30px}

/* hero */
.hero{top:80px;height:492px;background:linear-gradient(135deg,#2f8fd6 0%,#7cc3ee 45%,#d6ecf8 100%);overflow:hidden}
.hero-ride{right:0;top:0;width:640px;height:492px;background:radial-gradient(ellipse at 60% 40%,rgba(240,130,30,.55),rgba(240,130,30,0) 60%)}
.hero h1{left:110px;top:180px;font-size:58px;font-weight:700;color:var(--white);letter-spacing:2px;line-height:1}
.hero h2{left:110px;top:258px;font-size:36px;font-weight:600;color:var(--white)}
.btn-book{left:108px;top:338px;width:196px;height:46px;border-radius:23px;background:var(--white);color:var(--ink);font-weight:600;font-size:18px;display:flex;align-items:center;justify-content:center}
.mascot{background:linear-gradient(160deg,#f6a43a,#d97a1c);border-radius:45% 55% 40% 60%}

/* features */
.features{top:572px;height:413px}
.feature{top:105px;width:220px;text-align:center}
.feature svg{display:block;margin:0 auto}
.feature p{font-size:15px;font-weight:600;color:var(--ink);margin-top:16px}

/* shared section heads */
.grey{background:var(--grey-bg)}
.sec-title{left:110px;font-size:32px;font-weight:600;color:var(--ink);letter-spacing:.3px}
.sec-title::after{content:"";display:block;width:70px;height:5px;border-radius:3px;background:var(--yellow);margin-top:8px}
.arrows{right:110px;display:flex;gap:10px}
.arrows span{width:24px;height:24px;border:1.5px solid var(--ink);border-radius:50%;display:flex;align-items:center;justify-content:center;font-size:13px;line-height:1;color:var(--ink)}

/* tabs */
.tabs{left:110px;top:123px;width:980px;height:60px;background:var(--yellow);display:flex;align-items:center;gap:22px;padding-left:28px;font-size:14px;font-weight:500;color:var(--ink)}
.tabs .active{background:#fde3a0;padding:18px 14px;text-decoration:underline}

/* deal cards */
.card-row{left:112px;display:flex;gap:12px}
.deal-card{width:318px;text-align:center}
.deal-photo{height:268px;border-radius:12px;position:relative}
.tag{position:absolute;left:22px;font-size:10px;font-weight:600;color:var(--white);padding:4px 12px;border-radius:10px}
.tag.hot{top:24px;background:var(--yellow);color:var(--ink)}
.tag.seller{bottom:30px;background:var(--accent)}
.deal-card h3{font-size:14.5px;font-weight:500;color:var(--ink);line-height:1.6;margin:18px auto 0;width:240px}
.vendor{font-size:14px;color:var(--accent);margin-top:12px}
.rating{font-size:13px;color:var(--yellow);margin-top:4px}
.rating span{color:var(--text);font-size:11px;margin-left:8px}
.price{display:inline-block;margin-top:10px;background:var(--yellow);border-radius:12px;padding:2px 18px;font-size:14px;font-weight:500;color:var(--ink)}
.price s{color:var(--ink)}
.price b{font-weight:500;color:var(--accent)}

/* take me there */
.destinations{top:1712px;height:573px}
.place{top:150px;width:300px;text-align:center}
.place-photo{position:absolute;left:39px;top:0;width:222px;height:222px;border-radius:50%;border:14px solid var(--ink)}
.place svg{position:absolute;left:0;top:0}
.place p{position:absolute;top:290px;width:300px;font-size:15px;color:var(--ink);text-decoration:underline}

/* experiences you'll love */
.love{top:2960px;height:715px;background:var(--orange)}
.love .sec-title::after{background:var(--ink)}
.love .arrows span{border:none;font-size:26px}
.cat{width:300px}
.cat-photo{height:178px;border-radius:4px}
.cat p{font-size:18px;font-weight:600;color:var(--ink);margin-top:14px}

/* testimonials */
.testimonials{top:3675px;height:660px}
.review{top:180px;width:300px;text-align:center}
.review .avatar{position:relative;width:300px;height:190px}
.review .avatar div{position:absolute;left:68px;top:0;width:164px;height:164px;border-radius:50%;border:11px solid var(--ink)}
.review .avatar svg{position:absolute;left:0;top:0}
.review h4{font-size:18px;font-weight:600;color:var(--ink);margin-top:28px}
.review .stars{color:var(--yellow);font-size:20px;letter-spacing:3px}
.review p{font-size:14.5px;color:var(--muted);line-height:1.6;width:245px;margin:10px auto 0}

/* new experience */
.new-exp{top:4335px;height:685px}
.new-card{top:180px;width:292px;text-align:center}
.new-photo{height:312px;border-radius:10px;position:relative}
.meals{position:absolute;left:74px;bottom:8px;background:var(--accent);color:var(--white);font-size:10px;border-radius:10px;padding:3px 12px}
.new-card h3{font-size:15px;font-weight:500;color:var(--ink);line-height:1.55;margin-top:26px}
.new-card .from{font-size:15px;font-weight:600;color:var(--ink)}
.new-card .from b{color:var(--accent);font-weight:600}

/* footer */
.site-footer{top:5020px;height:332px;background:#000;color:var(--white);text-align:center}
.footer-brand{top:62px;left:0;width:1200px;font-size:46px;font-weight:700;letter-spacing:3px}
.footer-nav{top:185px;left:0;width:1200px;display:flex;justify-content:center;gap:84px;font-size:16px;font-weight:500}
.copyright{top:234px;left:0;width:1200px;font-size:12px}
.socials{top:270px;left:534px;display:flex;gap:14px}
.socials span{width:34px;height:34px;border-radius:50%;background:var(--yellow);display:block}
</style>
</head>
<body>

<header class="section site-header">
  <div class="abs menu-toggle"><span></span><span></span><span></span></div>
  <div class="abs brand">WAVELOOP TRIPS</div>
  <nav class="abs main-nav"><span>Destinations ▾</span><span>Experiences ▾</span><span class="hot">Hot Deals</span><span>Gifts ▾</span></nav>
  <div class="abs login">Log In <i></i></div>
  <svg class="abs head-icon" style="left:1040px" width="16" height="16" viewBox="0 0 16 16"><circle cx="6.5" cy="6.5" r="4.5" fill="none" stroke="#111" stroke-width="2"/><line x1="10" y1="10" x2="14" y2="14" stroke="#111" stroke-width="2"/></svg>
  <svg class="abs head-icon" style="left:1072px" width="16" height="16" viewBox="0 0 16 16"><path d="M1 2h3l2 8h7l2-6H5" fill="none" stroke="#111" stroke-width="2"/><circle cx="7" cy="13.5" r="1.5" fill="#111"/><circle cx="12" cy="13.5" r="1.5" fill="#111"/></svg>
</header>

<section class="section hero">
  <div class="abs hero-ride" role="img" aria-label="Orange roller coaster loop against a blue sky"></div>
  <h1 class="abs">WAVELOOP</h1>
  <h2 class="abs">Experience It All</h2>
  <a class="abs btn-book">Book Now</a>
</section>
<div class="abs mascot" style="left:0;top:420px;width:104px;height:212px" role="img" aria-label="Cartoon kangaroo mascot"></div>

<section class="section features">
  <div class="abs feature" style="left:95px">
    <svg width="150" height="150" viewBox="0 0 150 150"><path d="M10 75 A65 65 0 0 1 140 75" fill="none" stroke="#f9b91a" stroke-width="9"/><circle cx="75" cy="85" r="55" fill="none" stroke="#111" stroke-width="9"/><circle cx="75" cy="85" r="24" fill="none" stroke="#111" stroke-width="3"/><text x="75" y="94" text-anchor="middle" font-family="Poppins,sans-serif" font-size="24" fill="#111">$</text></svg>
    <p>Best Price Guaranteed</p>
  </div>
  <div class="abs feature" style="left:362px">
    <svg width="150" height="150" viewBox="0 0 150 150"><path d="M10 75 A65 65 0 0 1 140 75" fill="none" stroke="#f9b91a" stroke-width="9"/><circle cx="75" cy="85" r="55" fill="none" stroke="#111" stroke-width="9"/><path d="M75 58 L97 66 V84 C97 98 86 106 75 112 C64 106 53 98 53 84 V66 Z" fill="none" stroke="#111" stroke-width="3"/><path d="M65 85 L73 93 L87 77" fill="none" stroke="#111" stroke-width="3"/></svg>
    <p>Trusted By Thousands</p>
  </div>
  <div class="abs feature" style="left:627px">
    <svg width="150" height="150" viewBox="0 0 150 150"><path d="M10 75 A65 65 0 0 1 140 75" fill="none" stroke="#f9b91a" stroke-width="9"/><circle cx="75" cy="85" r="55" fill="none" stroke="#111" stroke-width="9"/><circle cx="75" cy="73" r="11" fill="none" stroke="#111" stroke-width="3"/><path d="M56 110 V100 C56 92 64 87 75 87 C86 87 94 92 94 100 V110" fill="none" stroke="#111" stroke-width="3"/></svg>
    <p>Australian Owned</p>
  </div>
  <div class="abs feature" style="left:893px">
    <svg width="150" height="150" viewBox="0 0 150 150"><path d="M10 75 A65 65 0 0 1 140 75" fill="none" stroke="#f9b91a" stroke-width="9"/><circle cx="75" cy="85" r="55" fill="none" stroke="#111" stroke-width="9"/><path d="M52 88 V80 A23 23 0 0 1 98 80 V88" fill="none" stroke="#111" stroke-width="3"/><rect x="62" y="72" width="26" height="18" rx="4" fill="none" stroke="#111" stroke-width="3"/><circle cx="69" cy="81" r="1.8" fill="#111"/><circle cx="75" cy="81" r="1.8" fill="#111"/><circle cx="81" cy="81" r="1.8" fill="#111"/></svg>
    <p>Unbeatable Support</p>
  </div>
</section>

<section class="section grey" style="top:985px;height:727px">
  <h2 class="abs sec-title" style="top:50px">TOP EXPERIENCES</h2>
  <div class="abs arrows" style="top:55px"><span>‹</span><span>›</span></div>
  <div class="abs tabs"><span class="active">Gold Coast</span><span>Carins</span><span>Port Duglas</span><span>Sunshine Coast</span><span>Whitsundays</span><span>Brisbane</span><span>Sydney</span><span>Adelaide</span><span>Hobart</span><span>Perth</span></div>
  <div class="abs card-row" style="top:210px">
    <article class="deal-card"><div class="deal-photo" role="img" aria-label="Family enjoying a theme park day" style="background:linear-gradient(160deg,#d9a07a,#6d8fb5)"><span class="tag hot">Hot Deal</span><span class="tag seller">★ Best Seller</span></div><h3>Sunvale Park, Splashcove World &amp; Skyreach Deck 3 Day Ticket</h3><p class="vendor">by Sunvale Park Tickets</p><div class="rating">★★★★★<span>4.9 Star</span></div><p class="price">from <s>$159.00</s> <b>$141.55</b></p></article>
    <article class="deal-card"><div class="deal-photo" role="img" aria-label="Roller coaster loop among trees" style="background:linear-gradient(160deg,#8fc3e6,#e08a2a 60%,#3f6b32)"><span class="tag hot">Hot Deal</span><span class="tag seller">★ Best Seller</span></div><h3>Sunvale Park, Splashcove World &amp; Skyreach Deck 3 Day Ticket</h3><p class="vendor">by Sunvale Park Tickets</p><div class="rating">★★★★★<span>4.9 Star</span></div><p class="price">from <s>$159.00</s> <b>$141.55</b></p></article>
    <article class="deal-card"><div class="deal-photo" role="img" aria-label="Child splashing in a water park" style="background:linear-gradient(160deg,#eecb5a,#3fa2dc 55%,#1d6fb0)"><span class="tag hot">Hot Deal</span><span class="tag seller">★ Best Seller</span></div><h3>Sunvale Park, Splashcove World &amp; Skyreach Deck 3 Day Ticket</h3><p class="vendor">by Sunvale Park Tickets</p><div class="rating">★★★★★<span>4.9 Star</span></div><p class="price">from <s>$159.00</s> <b>$141.55</b></p></article>
  </div>
</section>

<div class="abs" style="left:-90px;top:1660px;width:200px;height:230px;border-radius:50%;background:var(--beige)"></div>
<div class="abs mascot" style="left:0;top:1550px;width:110px;height:220px" role="img" aria-label="Cartoon kangaroo mascot waving"></div>

<section class="section destinations">
  <h2 class="abs sec-title" style="top:82px">TAKE ME THERE</h2>
  <div class="abs arrows" style="top:90px"><span>‹</span><span>›</span></div>
  <div class="abs place" style="left:110px"><svg width="300" height="270" viewBox="0 0 300 270"><path d="M10 150 A140 110 0 0 0 290 150" fill="none" stroke="#f9b91a" stroke-width="10"/></svg><div class="place-photo" role="img" aria-label="Turquoise tropical beach" style="background:linear-gradient(180deg,#7fc6ef,#2ab0b8 55%,#e8dcb5)"></div><p>Cairns</p></div>
  <div class="abs place" style="left:450px"><svg width="300" height="270" viewBox="0 0 300 270"><path d="M10 150 A140 110 0 0 0 290 150" fill="none" stroke="#f9b91a" stroke-width="10"/></svg><div class="place-photo" role="img" aria-label="Rainforest waterfall" style="background:linear-gradient(180deg,#4f8f2f,#1f4a1d 60%,#9bb8b0)"></div><p>Port Douglas</p></div>
  <div class="abs place" style="left:790px"><svg width="300" height="270" viewBox="0 0 300 270"><path d="M10 150 A140 110 0 0 0 290 150" fill="none" stroke="#f9b91a" stroke-width="10"/></svg><div class="place-photo" role="img" aria-label="Friends celebrating on a sunny coast" style="background:linear-gradient(180deg,#8cc7ee,#5f8fb3 55%,#2e3d52)"></div><p>Sunshine Coast</p></div>
</section>

<section class="section grey" style="top:2285px;height:675px">
  <h2 class="abs sec-title" style="top:50px;left:114px">TOP DEALS FOR YOU</h2>
  <div class="abs arrows" style="top:57px"><span>‹</span><span>›</span></div>
  <div class="abs card-row" style="top:155px">
    <article class="deal-card"><div class="deal-photo" role="img" aria-label="Kids with colourful balloons" style="background:linear-gradient(160deg,#e94b3c,#f2c84b 50%,#8a6bb5)"><span class="tag hot">Hot Deal</span><span class="tag seller">★ Best Seller</span></div><h3>Sunvale Park, Splashcove World &amp; Skyreach Deck 3 Day Ticket</h3><p class="vendor">by Sunvale Park Tickets</p><div class="rating">★★★★★<span>4.9 Star</span></div><p class="price">from <s>$159.00</s> <b>$141.55</b></p></article>
    <article class="deal-card"><div class="deal-photo" role="img" aria-label="Grandparent and child on a bumper car" style="background:linear-gradient(160deg,#6b6f78,#d8452f 60%,#f1a43a)"><span class="tag hot">Hot Deal</span><span class="tag seller">★ Best Seller</span></div><h3>Sunvale Park, Splashcove World &amp; Skyreach Deck 3 Day Ticket</h3><p class="vendor">by Sunvale Park Tickets</p><div class="rating">★★★★★<span>4.9 Star</span></div><p class="price">from <s>$159.00</s> <b>$141.55</b></p></article>
    <article class="deal-card"><div class="deal-photo" role="img" aria-label="Friends with cotton candy at a fair" style="background:linear-gradient(160deg,#f0b46a,#e58a9a 55%,#4a8fc9)"><span class="tag hot">Hot Deal</span><span class="tag seller">★ Best Seller</span></div><h3>Sunvale Park, Splashcove World &amp; Skyreach Deck 3 Day Ticket</h3><p class="vendor">by Sunvale Park Tickets</p><div class="rating">★★★★★<span>4.9 Star</span></div><p class="price">from <s>$159.00</s> <b>$141.55</b></p></article>
  </div>
</section>

<section class="section love">
  <h2 class="abs sec-title" style="top:70px;left:113px">EXPERIENCES YOU’LL LOVE</h2>
  <div class="abs arrows" style="top:70px;gap:26px"><span>‹</span><span>›</span></div>
  <div class="abs cat" style="left:105px;top:158px"><div class="cat-photo" role="img" aria-label="Family riding a jet ski" style="background:linear-gradient(160deg,#6aa7d6,#1e5c9a)"></div><p>Adventure Tours</p></div>
  <div class="abs cat" style="left:445px;top:158px"><div class="cat-photo" role="img" aria-label="Kayaker on a fjord" style="background:linear-gradient(180deg,#cfe3ee,#4c7d76 55%,#24535c)"></div><p>Outdoor Activities</p></div>
  <div class="abs cat" style="left:785px;top:158px"><div class="cat-photo" role="img" aria-label="Woman on a speedboat ride" style="background:linear-gradient(160deg,#4c9bdc,#c9e2f2 60%,#2b6fb0)"></div><p>Hot Deals</p></div>
  <div class="abs cat" style="left:105px;top:398px"><div class="cat-photo" role="img" aria-label="Family with a dog at a ranch" style="background:linear-gradient(160deg,#8a5a3a,#c98a55 60%,#3a2a20)"></div><p>Fun &amp; Games</p></div>
  <div class="abs cat" style="left:445px;top:398px"><div class="cat-photo" role="img" aria-label="Child watching fish at an aquarium" style="background:linear-gradient(160deg,#0f4f72,#1d86a8 55%,#0a2d45)"></div><p>Zoos &amp; Aquariums</p></div>
  <div class="abs cat" style="left:785px;top:398px"><div class="cat-photo" role="img" aria-label="Snorkellers on a reef" style="background:linear-gradient(160deg,#5fb3dc,#2a7ea8 60%,#c8b07a)"></div><p>Reef &amp; Island Cruises</p></div>
</section>

<div class="abs" style="left:1090px;top:3610px;width:220px;height:230px;border-radius:50%;background:var(--beige)"></div>
<div class="abs mascot" style="left:1095px;top:3525px;width:105px;height:205px" role="img" aria-label="Cartoon kangaroo mascot"></div>

<section class="section testimonials">
  <h2 class="abs sec-title" style="top:90px;left:112px">TESTIMONIALS</h2>
  <div class="abs arrows" style="top:97px"><span>‹</span><span>›</span></div>
  <div class="abs review" style="left:80px"><div class="avatar"><svg width="300" height="190" viewBox="0 0 300 190"><path d="M42 92 A108 90 0 0 0 258 92" fill="none" stroke="#f9b91a" stroke-width="9"/></svg><div role="img" aria-label="Customer portrait" style="background:linear-gradient(180deg,#6fa3c6,#2f5e7e)"></div></div><h4>Liam Harte</h4><div class="stars">★★★★★</div><p>Lorem ipsum dolor sit amet, consectetur adipiscing elit, sed do eiusmod tempor incididunt ut labore et dolore magna aliqua.</p></div>
  <div class="abs review" style="left:452px"><div class="avatar"><svg width="300" height="190" viewBox="0 0 300 190"><path d="M42 92 A108 90 0 0 0 258 92" fill="none" stroke="#f9b91a" stroke-width="9"/></svg><div role="img" aria-label="Customer portrait" style="background:linear-gradient(180deg,#d8c6b0,#8b6a4f)"></div></div><h4>Nora Vell</h4><div class="stars">★★★★★</div><p>Lorem ipsum dolor sit amet, consectetur adipiscing elit, sed do eiusmod tempor incididunt ut labore et dolore magna aliqua.</p></div>
  <div class="abs review" style="left:825px"><div class="avatar"><svg width="300" height="190" viewBox="0 0 300 190"><path d="M42 92 A108 90 0 0 0 258 92" fill="none" stroke="#f9b91a" stroke-width="9"/></svg><div role="img" aria-label="Customer portrait" style="background:linear-gradient(180deg,#c9d2db,#4b5560)"></div></div><h4>Ravi Anand</h4><div class="stars">★★★★★</div><p>Lorem ipsum dolor sit amet, consectetur adipiscing elit, sed do eiusmod tempor incididunt ut labore et dolore magna aliqua.</p></div>
</section>

<section class="section grey new-exp">
  <h2 class="abs sec-title" style="top:87px;left:112px">TOP NEW EXPERIENCE</h2>
  <div class="abs arrows" style="top:94px"><span>‹</span><span>›</span></div>
  <article class="abs new-card" style="left:112px"><div class="new-photo" role="img" aria-label="Couple relaxing on a boat deck" style="background:linear-gradient(160deg,#d9e8f2,#3c6f9e 55%,#f2efe8)"></div><h3>Gold Coast Zephra Jetboating Experience from Main Beach<br>45 Minutes by Zephra Jet</h3><p class="from">from <b>$89.00</b></p></article>
  <article class="abs new-card" style="left:455px"><div class="new-photo" role="img" aria-label="Sailor on a yacht bow at sunset" style="background:linear-gradient(180deg,#f3c4a2,#e9a77d 50%,#f4e4d6)"><span class="meals">Meals Included</span></div><h3>Gold Coast Zephra Jetboating Experience from Main Beach<br>45 Minutes by Zephra Jet</h3><p class="from">from <b>$89.00</b></p></article>
  <article class="abs new-card" style="left:798px"><div class="new-photo" role="img" aria-label="Rider on a water jet pack" style="background:linear-gradient(180deg,#eef2f5,#9fb2bf 55%,#2f4c5a)"></div><h3>Gold Coast Zephra Jetboating Experience from Main Beach<br>45 Minutes by Zephra Jet</h3><p class="from">from <b>$89.00</b></p></article>
</section>

<footer class="section site-footer">
  <div class="abs footer-brand">WAVELOOP TRIPS</div>
  <nav class="abs footer-nav"><span>Home</span><span>Destinations</span><span>Experiences</span><span>Hot Deals</span><span>Gifts</span><span>Contact Us</span></nav>
  <p class="abs copyright">(C) Copyright 2023 | All Rights Reserved.</p>
  <div class="abs socials"><span></span><span></span><span></span></div>
</footer>

</body>
</html>
```